Stationary For Accounting Firm
TALLORAN BREVIK PC
Professional
Jaspal T Varikh
Principal
482 W Orchard Ln Hightstown, NJ 08377
jvarikh@talloranbrevik.com
www.talloranbrevik.com
Only use my name, title, and email address on business card.

```html
<!DOCTYPE html>
<html lang="en">
<head>
<meta charset="utf-8">
<title>Talloran Brevik PC — Business Card</title>
<link rel="stylesheet" href="https://fonts.googleapis.com/css2?family=Didact+Gothic&display=swap">
<style>
  :root {
    --charcoal: #4c4d4f;
    --brand-blue: #1b72ba;
    --panel-pale: #cde1f1;
    --panel-sky: #a9c9e5;
    --ink-grey: #5a5b5d;
    --rule-grey: #8a8c8f;
    --white: #ffffff;
  }
  html, body {
    margin: 0;
    padding: 0;
    overflow: hidden;
    background: var(--charcoal);
  }
  .business-card {
    position: relative;
    width: 1200px;
    height: 686px;
    overflow: hidden;
    background: var(--charcoal);
    font-family: "Didact Gothic", "Century Gothic", sans-serif;
  }
  .card-graphics {
    position: absolute;
    inset: 0;
  }
  .firm-name {
    position: absolute;
    left: 30px;
    top: 432px;
    width: 560px;
    margin: 0;
    font-size: 66px;
    font-weight: 400;
    color: var(--ink-grey);
    text-align: center;
    white-space: nowrap;
    line-height: 1;
  }
  .firm-suffix {
    position: absolute;
    left: 30px;
    top: 512px;
    width: 560px;
    font-size: 16px;
    line-height: 1;
    color: var(--ink-grey);
    text-align: center;
    letter-spacing: 1px;
  }
  .firm-rule {
    position: absolute;
    left: 38px;
    top: 538px;
    width: 528px;
    height: 2px;
    background: var(--rule-grey);
  }
  .firm-services {
    position: absolute;
    left: 30px;
    top: 560px;
    width: 560px;
    font-size: 15px;
    line-height: 1;
    color: var(--ink-grey);
    text-align: center;
    letter-spacing: 6px;
    white-space: nowrap;
  }
  .contact-name {
    position: absolute;
    right: 55px;
    top: 470px;
    margin: 0;
    font-size: 38px;
    font-weight: 400;
    line-height: 1;
    color: var(--brand-blue);
    white-space: nowrap;
  }
  .contact-title {
    position: absolute;
    right: 55px;
    top: 530px;
    margin: 0;
    font-size: 36px;
    line-height: 1;
    color: var(--ink-grey);
  }
  .contact-email {
    position: absolute;
    right: 50px;
    top: 598px;
    margin: 0;
    font-size: 38px;
    line-height: 1;
    color: var(--white);
    white-space: nowrap;
  }
</style>
</head>
<body>
  <div class="business-card">
    <svg class="card-graphics" width="1200" height="686" viewBox="0 0 1200 686" aria-hidden="true">
      <polygon class="top-tab" points="0,43 492,43 520,133 0,133" fill="var(--brand-blue)"/>
      <rect class="panel-right" x="516" y="133" width="684" height="455" fill="var(--panel-sky)"/>
      <rect class="panel-left" x="0" y="133" width="516" height="455" fill="var(--panel-pale)"/>
      <rect class="brand-square" x="240" y="200" width="160" height="160" fill="var(--brand-blue)"/>
    </svg>

    <h1 class="firm-name">Talloran Brevik</h1>
    <div class="firm-suffix">PC</div>
    <div class="firm-rule"></div>
    <div class="firm-services">ACCOUNTING | TAX | ADVISORY</div>

    <h2 class="contact-name">Jaspal T Varikh</h2>
    <p class="contact-title">Principal</p>
    <p class="contact-email">jvarikh@talloranbrevik.com</p>
  </div>
</body>
</html>
```